Bookkeeping website design

We need a basic site design for wordpress.
We are a bookkeeping business and will need to present a look consistent with the colours and style of the logo.

Target Market(s)

Business owners

Industry/Entity Type

Accounting/Bookkeeping

Coding

Coded - Design and coding required

Number of Pages Required

1 page

```html
<!DOCTYPE html>
<html lang="en">
<head>
<meta charset="utf-8">
<title>Brightledger Bookkeeping</title>
<link rel="stylesheet" href="https://fonts.googleapis.com/css2?family=Montserrat:wght@400;500;600;700&family=Bebas+Neue&display=swap">
<style>
:root{
  --teal:#14c3ea;
  --green:#8dc63f;
  --brand-grad:linear-gradient(90deg,#14c3ea 0%,#8dc63f 100%);
  --ink:#111;
  --muted:#555;
  --soft:#f4f5f5;
  --footer:#0e1a20;
  --white:#fff;
}
*{box-sizing:border-box;margin:0;padding:0}
html,body{width:1200px;height:3352px;overflow:hidden}
body{position:relative;font-family:"Montserrat",sans-serif;color:var(--ink);background:var(--white)}
.abs{position:absolute}
.btn{position:absolute;display:flex;align-items:center;justify-content:center;border-radius:30px;background:linear-gradient(90deg,#8dc63f,#14c3ea);color:#fff;font-size:15px;font-weight:500}
.eyebrow{position:absolute;left:0;width:1200px;text-align:center;color:var(--green);font-size:15px;font-weight:600}
.section-title{position:absolute;left:0;width:1200px;text-align:center;font-size:30px;font-weight:600;letter-spacing:.3px}
.ph{position:absolute}

/* top bar & nav */
.topbar{left:0;top:0;width:1200px;height:29px;background:var(--brand-grad)}
.social-mini{top:4px;width:22px;height:22px;border:1.5px solid #fff;border-radius:50%;color:#fff;font-size:11px;font-weight:700;display:flex;align-items:center;justify-content:center}
.top-phone{left:948px;top:6px;color:#fff;font-size:14px;font-weight:600;display:flex;gap:6px;align-items:center}
.top-login{left:1082px;top:6px;color:#fff;font-size:13px;display:flex;gap:6px;align-items:center}
.nav{left:0;top:29px;width:1200px;height:62px;background:#fff;box-shadow:0 1px 4px rgba(0,0,0,.06)}
.nav a{position:absolute;top:25px;font-size:12px;color:#222;text-decoration:none}
.nav .home{left:298px;top:18px;width:65px;height:31px;border-radius:16px;background:linear-gradient(90deg,#14c3ea,#8dc63f);color:#fff;display:flex;align-items:center;justify-content:center}
.logo-tab{left:506px;top:13px;width:188px;height:78px;background:#fff;border-radius:14px 14px 0 0}
.wordmark{position:absolute;display:flex;align-items:center;gap:8px;font-weight:700;color:var(--teal)}
.wordmark .dot{width:16px;height:16px;border-radius:50%;background:var(--green)}

/* hero */
.hero{left:0;top:91px;width:1200px;height:620px;overflow:hidden}
.hero-photo{left:0;top:0;width:1200px;height:620px;background:linear-gradient(120deg,#3e4e63 0%,#c7ccd4 35%,#e9ecef 60%,#f3f3f1 100%)}
.hero-circle{left:726px;top:44px;width:412px;height:412px;border-radius:50%;background:rgba(255,255,255,.9)}
.hero-kicker{left:726px;top:120px;width:412px;text-align:center;font-family:"Bebas Neue",sans-serif;font-size:56px;line-height:53px;background:linear-gradient(90deg,#14c3ea,#8dc63f);-webkit-background-clip:text;background-clip:text;color:transparent}
.hero-sub{left:726px;top:238px;width:412px;text-align:center;font-size:23px;font-weight:600}
.hero-text{left:790px;top:279px;width:284px;text-align:center;font-size:12.5px;line-height:19.5px;color:#333}
.arrow{width:38px;height:38px;border-radius:50%;display:flex;align-items:center;justify-content:center}

/* services */
.card{position:absolute;top:849px;width:224px;height:322px;background:#fff;box-shadow:0 2px 12px rgba(0,0,0,.09)}
.card .ph{left:4px;top:4px;width:216px;height:157px}
.card h3{position:absolute;left:12px;top:180px;font-size:16.5px;font-weight:600}
.card p{position:absolute;left:12px;top:214px;width:200px;font-size:11.5px;line-height:20px;color:#555}
.card a{position:absolute;left:14px;top:281px;font-size:11.5px;color:var(--green);font-weight:600}

/* cta band */
.cta{left:117px;top:1249px;width:966px;height:131px;border-radius:70px 0 70px 0;background:var(--brand-grad)}
.cta h2{position:absolute;left:70px;top:26px;color:#fff;font-size:31px;font-weight:500}
.cta p{position:absolute;left:70px;top:66px;width:340px;color:#fff;font-size:13px;line-height:21px}
.cta .field{position:absolute;left:449px;top:45px;width:456px;height:43px;border-radius:22px;background:#fff}
.field span{position:absolute;left:22px;top:14px;font-size:11px;color:#888}

/* about */
.about-copy{left:687px}
.about-copy p{font-size:12px;line-height:20px;color:#555;width:355px}

/* benefits */
.benefit-tile{position:absolute;top:2026px;width:78px;height:78px;background:#fff;border-radius:8px;box-shadow:0 2px 10px rgba(0,0,0,.07);display:flex;align-items:center;justify-content:center}
.benefit-label{position:absolute;top:2132px;width:200px;text-align:center;font-size:14.5px;font-weight:600;line-height:21px}

/* testimonials */
.quote-box{left:206px;top:2477px;width:397px;height:260px;border:1.5px solid #5fd1ea;border-radius:18px;background:#eafafd}
.quote-box p{position:absolute;left:42px;top:66px;width:325px;font-size:11.5px;line-height:22px;color:#555}
.avatar{border-radius:50%}

/* footer */
.footer{left:0;top:2960px;width:1200px;height:346px;background:linear-gradient(180deg,#0c1a21,#142731)}
.foot-head{position:absolute;top:3084px;color:var(--teal);font-size:15px;font-weight:600}
.foot-list{position:absolute;left:334px;top:3128px;list-style:none}
.foot-list li{font-size:11.5px;color:#ddd;height:24px;display:flex;align-items:center;gap:12px}
.foot-list li::before{content:"";width:5px;height:5px;border:1.5px solid var(--green);border-radius:50%}
.foot-contact{position:absolute;left:544px;color:#ddd;font-size:11.5px;line-height:19px}
.foot-cta{left:778px;top:3020px;width:362px;height:240px;background:rgba(30,60,70,.75)}
.foot-cta h4{position:absolute;left:24px;top:24px;width:320px;color:#fff;font-size:19px;font-weight:500;line-height:26px}
.foot-cta .field{position:absolute;left:17px;top:118px;width:322px;height:40px;border-radius:20px;background:#fff}
.bottom-bar{left:0;top:3306px;width:1200px;height:46px;background:var(--brand-grad);color:#fff;font-size:11px;display:flex;align-items:center;justify-content:center}
.soc{position:absolute;top:3218px;width:38px;height:38px;border-radius:50%;background:var(--green);color:#fff;font-weight:700;font-size:15px;display:flex;align-items:center;justify-content:center}
</style>
</head>
<body>

<header>
  <div class="abs topbar"></div>
  <div class="abs social-mini" style="left:62px">f</div>
  <div class="abs social-mini" style="left:92px">in</div>
  <div class="abs top-phone">
    <svg width="14" height="14" viewBox="0 0 24 24"><path fill="#fff" d="M6.6 10.8a15 15 0 0 0 6.6 6.6l2.2-2.2c.3-.3.7-.4 1-.2 1.1.4 2.3.6 3.6.6.6 0 1 .4 1 1V20c0 .6-.4 1-1 1A17 17 0 0 1 3 4c0-.6.4-1 1-1h3.5c.6 0 1 .4 1 1 0 1.3.2 2.5.6 3.6.1.3 0 .7-.2 1z"/></svg>
    123 456 7890
  </div>
  <div class="abs top-login">
    <svg width="16" height="16" viewBox="0 0 24 24" fill="none" stroke="#fff" stroke-width="2"><circle cx="12" cy="12" r="10"/><circle cx="12" cy="10" r="3"/><path d="M6 19c1.5-3 10.5-3 12 0"/></svg>
    Login
  </div>
  <nav class="abs nav">
    <a class="home" href="#">Home</a>
    <a href="#" style="left:387px">About</a>
    <a href="#" style="left:438px">Services</a>
    <a href="#" style="left:713px">Benefits</a>
    <a href="#" style="left:777px">Testimonials</a>
    <a href="#" style="left:868px">Contact Us</a>
  </nav>
  <div class="abs logo-tab"></div>
  <div class="wordmark" style="left:525px;top:48px;font-size:20px"><span class="dot"></span>Brightledger</div>
</header>

<section class="abs hero">
  <div class="ph hero-photo" role="img" aria-label="Photo of two colleagues reviewing financial reports at a laptop in an office"></div>
  <div class="abs hero-circle"></div>
  <div class="abs hero-kicker">YOU RUN YOUR<br>BUSINESS.</div>
  <div class="abs hero-sub">We'll Handle Your Finance.</div>
  <p class="abs hero-text">From bookkeeping to tax filling, Brightledger is the all-in-one finacial toolkit your business can count on.</p>
  <div class="btn" style="left:861px;top:351px;width:142px;height:40px">GET STARTED</div>
  <div class="abs arrow" style="left:40px;top:224px;background:#6da53a">
    <svg width="14" height="14" viewBox="0 0 24 24"><path d="M15 4 7 12l8 8" stroke="#fff" stroke-width="2.5" fill="none"/></svg>
  </div>
  <div class="abs arrow" style="left:1121px;top:224px;background:#1d2a33">
    <svg width="14" height="14" viewBox="0 0 24 24"><path d="m9 4 8 8-8 8" stroke="#fff" stroke-width="2.5" fill="none"/></svg>
  </div>
  <svg class="abs" style="left:0;top:440px" width="1200" height="180" viewBox="0 0 1200 180">
    <path d="M0 170 V160 C150 210 350 120 560 90 C800 55 1000 30 1200 60 V180 Z" fill="#fff"/>
    <path d="M0 90 C80 150 220 160 360 130 C560 90 760 30 960 20 C1060 15 1140 25 1200 45 V60 C1100 20 980 30 860 50 C680 80 520 130 340 160 C200 180 70 160 0 130 Z" fill="#14c3ea"/>
    <path d="M700 120 C820 80 960 60 1040 70 C1100 80 1130 100 1145 125 C1110 100 1050 88 960 92 C860 97 780 110 700 120 Z" fill="#8dc63f"/>
  </svg>
</section>

<section>
  <div class="eyebrow" style="top:754px">We Are Expert In</div>
  <h2 class="section-title" style="top:780px">OUR SERVICES</h2>

  <article class="card" style="left:117px">
    <div class="ph" role="img" aria-label="Photo of hands using a calculator" style="background:linear-gradient(135deg,#3b3b3b,#b79b7d)"></div>
    <h3>IncomeTax</h3>
    <p>Lorem Ipsum has been the indust standard dummy text ever since is the when an unknown.</p>
    <a>know More</a>
  </article>
  <article class="card" style="left:364px">
    <div class="ph" role="img" aria-label="Photo of a businessman holding documents" style="background:linear-gradient(135deg,#d9dcdc,#2d2f33)"></div>
    <h3>Financial Audit</h3>
    <p>Lorem Ipsum has been the indust standard dummy text ever since is the when an unknown.</p>
    <a>know More</a>
  </article>
  <article class="card" style="left:612px">
    <div class="ph" role="img" aria-label="Photo of a laptop showing charts" style="background:linear-gradient(135deg,#b9b4ad,#e6ebee)"></div>
    <h3>Outsourced CFO</h3>
    <p>Lorem Ipsum has been the indust standard dummy text ever since is the when an unknown.</p>
    <a>know More</a>
  </article>
  <article class="card" style="left:860px">
    <div class="ph" role="img" aria-label="Photo of a person signing financial papers" style="background:linear-gradient(135deg,#4a3a30,#dfe3e8)"></div>
    <h3>Business Valuation</h3>
    <p>Lorem Ipsum has been the indust standard dummy text ever since is the when an unknown.</p>
    <a>know More</a>
  </article>
</section>

<section class="abs cta">
  <h2>GET STARTED</h2>
  <p>Join thousands of small business owners who trust Brightledger with their bookkeeping.</p>
  <div class="field"><span>Enter Email *</span></div>
  <div class="btn" style="left:763px;top:45px;width:142px;height:43px">GET STARTED</div>
</section>

<section>
  <svg class="abs" style="left:188px;top:1462px" width="360" height="360" viewBox="0 0 360 360">
    <defs><linearGradient id="ring" x1="0" y1="1" x2="1" y2="0"><stop offset="0" stop-color="#14c3ea"/><stop offset="1" stop-color="#8dc63f"/></linearGradient></defs>
    <circle cx="180" cy="180" r="160" fill="none" stroke="url(#ring)" stroke-width="38"/>
  </svg>
  <div class="ph" role="img" aria-label="Photo of a cheerful man pointing at a laptop showing the website" style="left:170px;top:1448px;width:485px;height:374px;border-radius:40% 40% 12px 12px;background:linear-gradient(160deg,rgba(230,230,230,.95),rgba(200,205,210,.9))"></div>

  <div class="abs about-copy" style="top:1459px;color:var(--green);font-size:15px;font-weight:600">About Us</div>
  <h2 class="abs about-copy" style="top:1489px;font-size:30px;font-weight:600">BRIGHTLEDGER BOOKKEEPING</h2>
  <div class="abs about-copy" style="top:1541px">
    <p>Lorem Ipsum has been the industry's standard dummy text ever since the 1500s, when an unknown printer took a galley of typescrambled it to make a type specimen.</p>
    <p style="margin-top:12px">Lorem Ipsum has been the industry's standard dummy text ever since the 1500s, when an unknown printer took a galley of type and scrambled it to make a type specimen book. It has survived not only five centuries,also.</p>
  </div>
  <div class="btn" style="left:687px;top:1711px;width:142px;height:42px">LEARN MORE</div>
</section>

<section>
  <svg class="abs" style="left:0;top:1810px" width="1200" height="500" viewBox="0 0 1200 500">
    <path d="M0 15 C200 -10 420 60 640 50 C860 40 1040 0 1200 20 V440 C1040 400 880 430 700 460 C480 500 220 420 0 420 Z" fill="#f4f5f5"/>
  </svg>
  <div class="eyebrow" style="top:1934px;color:var(--teal)">Why Us</div>
  <h2 class="section-title" style="top:1958px">BENEFITS</h2>

  <div class="benefit-tile" style="left:189px" role="img" aria-label="Relaxed tax season icon">
    <svg width="44" height="44" viewBox="0 0 24 24" fill="none" stroke="#222" stroke-width="1.6"><circle cx="12" cy="12" r="10"/><path d="m7.5 12.5 3 3 6-6.5"/></svg>
  </div>
  <div class="benefit-tile" style="left:436px" role="img" aria-label="Finance overview icon">
    <svg width="44" height="44" viewBox="0 0 24 24" fill="none" stroke="#222" stroke-width="1.6"><path d="M4 20V10M10 20V5M16 20v-7"/><circle cx="18" cy="7" r="4" fill="#8dc63f" stroke="none"/></svg>
  </div>
  <div class="benefit-tile" style="left:679px" role="img" aria-label="Money bag icon">
    <svg width="44" height="44" viewBox="0 0 24 24" fill="none" stroke="#222" stroke-width="1.6"><path d="M9 3h6l-2 4h-2zM11 7C6 9 4 14 5 18c.5 2 2 3 4 3h6c2 0 3.5-1 4-3 1-4-1-9-6-11"/><circle cx="12" cy="15" r="3.5" fill="#8dc63f" stroke="none"/></svg>
  </div>
  <div class="benefit-tile" style="left:936px" role="img" aria-label="Calculator icon">
    <svg width="44" height="44" viewBox="0 0 24 24" fill="none" stroke="#222" stroke-width="1.6"><rect x="7" y="2" width="13" height="19" rx="1.5"/><path d="M9.5 5h8v3h-8zM10 11h1M13 11h1M16 11h1M10 14h1M13 14h1M16 14h1M13 17h1M16 17h1"/><circle cx="6.5" cy="16.5" r="4" fill="#8dc63f" stroke="none"/></svg>
  </div>

  <div class="benefit-label" style="left:128px">No Stress Tax<br>Season</div>
  <div class="benefit-label" style="left:375px">Know Your<br>Financial</div>
  <div class="benefit-label" style="left:618px">Monthly Payment<br>Handled</div>
  <div class="benefit-label" style="left:875px">Accurate &amp; Effective<br>Bookkeeping</div>
</section>

<section>
  <div class="eyebrow" style="top:2335px;color:var(--teal)">Testimonials</div>
  <h2 class="section-title" style="top:2366px">WHAT OUR CLIENT SAY</h2>

  <div class="abs quote-box">
    <p>“ Lorem Ipsum has been the industry's standard textin dummy text ever since the 1500s, when anunk nown o printer took a galley of type and scrambled it to make a type specimen book. It has survived not only five the centuries, but also the leap into has been the industr industry's standard dummy text ever since the 1500s, when an unknown printer took a galley of type and scrambled it printing text indsut... ”</p>
  </div>
  <div class="abs" style="left:224px;top:2408px;font-family:Georgia,serif;font-size:130px;line-height:130px;font-weight:700;background:linear-gradient(90deg,#14c3ea,#8dc63f);-webkit-background-clip:text;background-clip:text;color:transparent">“</div>
  <svg class="abs" style="left:160px;top:2604px" width="16" height="24" viewBox="0 0 16 24"><path d="M13 2 3 12l10 10" stroke="#aaa" stroke-width="1.5" fill="none"/></svg>
  <svg class="abs" style="left:624px;top:2604px" width="16" height="24" viewBox="0 0 16 24"><path d="m3 2 10 10L3 22" stroke="#8dc63f" stroke-width="1.5" fill="none"/></svg>

  <div class="ph avatar" role="img" aria-label="Client portrait" style="left:241px;top:2764px;width:56px;height:56px;background:linear-gradient(135deg,#6b4a3a,#4fa3d8)"></div>
  <div class="abs" style="left:314px;top:2784px;width:12px;height:2px;background:#111"></div>
  <div class="abs" style="left:336px;top:2777px;font-size:13px;font-weight:600">CLIENT NAME</div>
  <div class="abs" style="left:336px;top:2796px;font-size:11.5px;color:var(--green)">Something.com</div>

  <div class="ph avatar" role="img" aria-label="Client portrait" style="left:724px;top:2475px;width:118px;height:118px;background:linear-gradient(135deg,#f0f4f6,#3f8fd2)"></div>
  <div class="ph avatar" role="img" aria-label="Client portrait" style="left:856px;top:2445px;width:146px;height:146px;background:linear-gradient(135deg,#bfc4c8,#6b5448)"></div>
  <div class="ph avatar" role="img" aria-label="Client portrait" style="left:1007px;top:2519px;width:76px;height:76px;background:linear-gradient(135deg,#5e8fb0,#a9a39d)"></div>
  <div class="ph avatar" role="img" aria-label="Client portrait" style="left:743px;top:2620px;width:192px;height:192px;background:linear-gradient(135deg,#7c8890,#3a4c66)"></div>
  <div class="ph avatar" role="img" aria-label="Client portrait" style="left:930px;top:2605px;width:120px;height:120px;background:linear-gradient(135deg,#d8dadd,#c27a3a)"></div>
</section>

<footer>
  <div class="abs footer"></div>
  <svg class="abs" style="left:0;top:2880px" width="1200" height="140" viewBox="0 0 1200 140">
    <path d="M0 0 H1200 V30 C1000 40 800 120 560 130 C340 140 160 110 0 80 Z" fill="#fff"/>
    <path d="M0 80 C160 110 340 140 560 130 C800 120 1000 40 1200 30 V52 C1000 70 820 130 570 140 C340 148 160 120 0 105 Z" fill="#14c3ea"/>
    <path d="M55 20 C110 70 210 100 330 98 C230 110 120 90 55 20 Z" fill="#8dc63f"/>
  </svg>

  <div class="wordmark" style="left:86px;top:3156px;font-size:26px"><span class="dot" style="width:20px;height:20px"></span>Brightledger</div>
  <div class="soc" style="left:155px">f</div>
  <div class="soc" style="left:200px">in</div>

  <div class="foot-head" style="left:334px">SITEMAP</div>
  <ul class="foot-list">
    <li>Home</li><li>About Us</li><li>Services</li><li>Work Gallery</li><li>News</li><li>Contact Us</li>
  </ul>

  <div class="foot-head" style="left:544px">CONTACT US</div>
  <svg class="abs" style="left:544px;top:3136px" width="16" height="22" viewBox="0 0 24 32"><path d="M12 2a9 9 0 0 0-9 9c0 7 9 19 9 19s9-12 9-19a9 9 0 0 0-9-9z" fill="none" stroke="#8dc63f" stroke-width="2.5"/><circle cx="12" cy="11" r="3.5" fill="#8dc63f"/></svg>
  <div class="foot-contact" style="left:579px;top:3124px">Brightledger<br>101 - Lorem ipsum simple text<br>print type setting Industry.</div>
  <svg class="abs" style="left:544px;top:3203px" width="18" height="18" viewBox="0 0 24 24"><path fill="#8dc63f" d="M6.6 10.8a15 15 0 0 0 6.6 6.6l2.2-2.2c.3-.3.7-.4 1-.2 1.1.4 2.3.6 3.6.6.6 0 1 .4 1 1V20c0 .6-.4 1-1 1A17 17 0 0 1 3 4c0-.6.4-1 1-1h3.5c.6 0 1 .4 1 1 0 1.3.2 2.5.6 3.6.1.3 0 .7-.2 1z"/></svg>
  <div class="foot-contact" style="left:579px;top:3201px;font-size:16px">123 456 7890</div>
  <svg class="abs" style="left:544px;top:3241px" width="18" height="14" viewBox="0 0 24 18"><rect width="24" height="18" rx="2" fill="#8dc63f"/><path d="m2 3 10 7 10-7" stroke="#0e1a20" stroke-width="2" fill="none"/></svg>
  <div class="foot-contact" style="left:579px;top:3238px">info@brightledger.com</div>

  <div class="abs foot-cta">
    <h4>Join thousands of small business Owners who trust Brightledger with Their bookkeeping.</h4>
    <div class="field"><span>Enter Email *</span></div>
    <div class="btn" style="left:17px;top:169px;width:141px;height:39px">GET STARTED</div>
  </div>

  <div class="abs bottom-bar">©NORTHFIELD STUDIO -2021 Allrights reserved.</div>
</footer>

</body>
</html>
```